Harbor Geriatric care need Business card design

Simple and elegance looking business card (colour choice will be very important)
Harbor geriatric care is medical consultation service for elderly population.

1st side---business logo and the doctor name/tile
eg: dr. XXX
MBBS,FRACP etc
Main room:
suite xxx AAA medical centre 18 XXX road Vic 3000
Phone:
Fax:

2nd side --different clinic address (up to 3 addresses) and need to have appointment time/ date

Suite xxx AAA medical centre , 18 XXX road VIC 3000

Please see attachment for business logo

Important: need to be compatible with Marlo Press for printing purpose.

Thank you.

hi, please look at the sample business card and create something similar. Company name: Harbor Geriatric Care PTY LTD ABN 47690518 ( all small font and no need to be obvious) company logo need to be obvious Apart from steady in support, also add Geriatrician for Community and Residential Care. Main room Dunova Medical Centre suite 2.14 204-206 Pelling street Box Hill Vic All appointment and enquiries: tel: 947160258 Fasmile: www.qwxplomz.com.au Kellwyn Medical Centre 42 dunmore road kellwyn VIC Ridgefield Care Frankston 587 Pellham road , franskton VIC 3199 Orchard Private Hospital specialist room 264 Tollard Road, Mt. Orchard VIC 3333 Dr. PN 80917kt DR. HW r8026179mm DR. GT 907612mm Thank you

```html
<!DOCTYPE html>
<html lang="en">
<head>
<meta charset="utf-8">
<title>Harbor Geriatric Care – Business Card</title>
<link rel="stylesheet" href="https://fonts.googleapis.com/css2?family=Arimo:wght@400;700&family=Lora:wght@500&display=swap">
<style>
  :root {
    --navy: #27367f;
    --navy-deep: #1e2a68;
    --red: #d42a3a;
    --ink: #2b3a86;
    --grey: #a7a9b3;
    --paper: #ffffff;
    --backdrop: #e9e7e2;
  }
  * { margin: 0; padding: 0; box-sizing: border-box; }
  html, body { width: 1200px; height: 885px; overflow: hidden; }
  body {
    background: var(--backdrop);
    font-family: "Arimo", Arial, sans-serif;
    position: relative;
  }
  .card {
    position: absolute;
    left: 300px;
    width: 600px;
    height: 367px;
    background: var(--paper);
    overflow: hidden;
    box-shadow: 0 6px 18px rgba(0,0,0,.18);
  }
  .card--front { top: 54px; }
  .card--back { top: 464px; }
  .card__shape { position: absolute; inset: 0; width: 100%; height: 100%; }

  .brand { position: absolute; display: flex; align-items: center; gap: 10px; }
  .brand__dot { width: 22px; height: 22px; border-radius: 50%; background: var(--red); flex: none; }
  .brand__name {
    font-family: "Lora", Georgia, serif;
    font-weight: 500;
    font-size: 34px;
    color: var(--ink);
    white-space: nowrap;
    letter-spacing: .2px;
  }
  .brand__tagline {
    position: absolute;
    font-size: 11px;
    letter-spacing: 6px;
    color: var(--grey);
    text-transform: uppercase;
    white-space: nowrap;
  }

  /* front */
  .card--front .brand { left: 62px; top: 62px; }
  .card--front .brand__tagline { left: 200px; top: 112px; }
  .contact {
    position: absolute;
    right: 34px;
    top: 150px;
    text-align: right;
    color: var(--ink);
    font-size: 16px;
    line-height: 25px;
  }
  .contact__row { display: flex; justify-content: flex-end; align-items: center; gap: 10px; }
  .contact__icon { width: 14px; height: 14px; flex: none; }
  .contact__address { margin-top: 4px; }
  .doctor {
    position: absolute;
    left: 40px;
    bottom: 30px;
    color: #fff;
  }
  .doctor__name { font-weight: 700; font-size: 25px; letter-spacing: .3px; white-space: nowrap; }
  .doctor__title { font-size: 15px; margin-top: 4px; }

  /* back */
  .card--back .brand { left: 36px; top: 36px; }
  .card--back .brand__tagline { left: 174px; top: 84px; }
  .appointment {
    position: absolute;
    left: 36px;
    top: 126px;
    color: var(--ink);
    font-size: 15px;
  }
  .appointment__label { margin-bottom: 8px; }
  .appointment__row { display: flex; align-items: flex-end; gap: 6px; }
  .appointment__line { display: inline-block; border-bottom: 1px solid var(--ink); height: 15px; }
  .appointment__line--date { width: 190px; }
  .appointment__line--time { width: 140px; }
  .clinics {
    position: absolute;
    left: 36px;
    top: 212px;
    list-style: none;
    color: var(--ink);
    font-size: 15px;
    line-height: 27px;
    white-space: nowrap;
  }
</style>
</head>
<body>

<section class="card card--front" aria-label="Business card front">
  <svg class="card__shape" viewBox="0 0 600 367" preserveAspectRatio="none" aria-hidden="true">
    <path d="M0,176 C200,286 400,316 600,286" fill="none" stroke="var(--red)" stroke-width="6"/>
    <path d="M0,192 C200,302 400,332 600,302 L600,367 L0,367 Z" fill="var(--navy)"/>
  </svg>

  <div class="brand">
    <span class="brand__dot"></span>
    <span class="brand__name">Harbor Geriatric Care</span>
  </div>
  <span class="brand__tagline">Steady in support</span>

  <div class="contact">
    <div class="contact__row">
      <span>xxxx xxx xxx</span>
      <svg class="contact__icon" viewBox="0 0 24 24" aria-label="Phone"><path fill="var(--red)" d="M6.6 10.8a15 15 0 0 0 6.6 6.6l2.2-2.2c.3-.3.7-.4 1-.2 1.1.4 2.3.6 3.6.6.6 0 1 .4 1 1V20c0 .6-.4 1-1 1A17 17 0 0 1 3 4c0-.6.4-1 1-1h3.5c.6 0 1 .4 1 1 0 1.3.2 2.5.6 3.6.1.3 0 .7-.2 1z"/></svg>
    </div>
    <div class="contact__row">
      <span>xxxx xxx xxx</span>
      <svg class="contact__icon" viewBox="0 0 24 24" aria-label="Fax"><path fill="var(--red)" d="M6 3h10v5H6zM3 9h18v10H3zm3 6v6h12v-6z"/></svg>
    </div>
    <div class="contact__address">suite xxx AAA medical centre<br>18 XXX road Vic 3000</div>
  </div>

  <div class="doctor">
    <div class="doctor__name">Employee Name</div>
    <div class="doctor__title">MBBS,FRACP</div>
  </div>
</section>

<section class="card card--back" aria-label="Business card back">
  <svg class="card__shape" viewBox="0 0 600 367" preserveAspectRatio="none" aria-hidden="true">
    <path d="M450,0 L600,0 L600,367 L598,367 C595,200 555,80 450,0 Z" fill="var(--navy)"/>
    <path d="M430,0 C540,80 582,200 586,367" fill="none" stroke="var(--red)" stroke-width="6"/>
  </svg>

  <div class="brand">
    <span class="brand__dot"></span>
    <span class="brand__name">Harbor Geriatric Care</span>
  </div>
  <span class="brand__tagline">Steady in support</span>

  <div class="appointment">
    <div class="appointment__label">Appointment</div>
    <div class="appointment__row">
      <span>Date:</span><span class="appointment__line appointment__line--date"></span>
      <span>Time:</span><span class="appointment__line appointment__line--time"></span>
    </div>
  </div>

  <ul class="clinics">
    <li>Suite xxx AAA medical centre , 18 XXX road VIC 3000</li>
    <li>Suite xxx AAA medical centre , 18 XXX road VIC 3000</li>
    <li>Suite xxx AAA medical centre , 18 XXX road VIC 3000</li>
  </ul>
</section>

</body>
</html>
```